Moulding supply company needs a Door Hanger Design

Door Hanger Design Request from Ledge Craft
www. ledgecrafts.example
We are moulding factory outlet in Toronto. Provide high quality moulding materials with competitive price like crown mouldings, casings, wainscoting, flatstocks, baseboards. We also provide professional installation for our clients. This door hanger will help the home owner easily find a local factory supplier with providing the materials as well as installation.

Detail request for design:
Size: 4”x11”, vertical
Shape: Rectangle

Content:
Front
1. Logo, see attachment(Use the left one, horizontal one)
2. Moulding factory outlet direct sale
3. Supply high quality Crown mouldings, baseboards, casings and wainscotings with competitive price
4. Installation & delivery
#2 content is the most important content, should be bold and readable
#3 can be smaller font compare to #2

Address: 47 North Willow Vale Rd, Richmond Hill, ON L4B 3K9
Telephone: 416 555 0143
416 555 0187
Email: info@ledgecrafts.example

Back
Slogan: Convert plain room into designer’s interiors

Telephone: 416 555 0143
416 555 0187
Email: info@ledgecrafts.example

Images:
Front
1. Display our productions for crown mouldings, baseboards, casings and wainscotings, refer to our website www.ledgecrafts.example. (The winner finally we will provide the high resolution images, low resolution please copy from our website so far)
Back
2. Display 4-6 nice images for 1. wainscoting walls 2. feature walls, 3. waffle ceiling like attached below. BUT PLEASE DON'T USE THE IMAGES PROVIDED, THIS IS ONLY A SAMPLE. Please use high resolution images for printing. ALSO PLEASE DON'T LIMIT YOUR CREATIVITY TO USE 4 SQUARES LIKE BELOW IMAGES. Please provide more ideas

Note:
1. Please do the bleeding for final printing production
2. Images have to be high resolution for ready to print
3. Style need to be fresh, clean, easy to read, modern and magazine style
4. Information has to be readable, easy to find, front and back both need to display company address, telephone, email, you can use icon or abbreviation to do these information.

Thanks,
Ledge Crafts

```html
<!DOCTYPE html>
<html lang="en">
<head>
<meta charset="utf-8">
<title>Ledge Crafts – Door Hanger</title>
<link rel="stylesheet" href="https://fonts.googleapis.com/css2?family=Bebas+Neue&family=Montserrat:wght@500;600&display=swap">
<style>
  :root {
    --stage: #2b2b2d;
    --paper: #f6f6f5;
    --red: #f1361d;
    --navy: #232c8c;
    --ink: #151515;
    --logo-grey: #4b5057;
    --photo-light: #e6ded3;
    --photo-mid: #b89f84;
    --photo-dark: #6b4a30;
  }
  * { margin: 0; padding: 0; box-sizing: border-box; }
  html, body { width: 1200px; height: 1093px; overflow: hidden; background: var(--stage); }
  .hanger {
    position: absolute; top: 89px; width: 332px; height: 914px;
    background: var(--paper); overflow: hidden;
    font-family: "Montserrat", sans-serif; color: var(--ink);
  }
  .hanger--front { left: 233px; background: linear-gradient(200deg, #ffffff 0%, #f3f3f3 45%, #f7f7f7 100%); }
  .hanger--back { left: 635px; }
  .hanger__cutout { position: absolute; left: 0; top: 0; }

  .headline {
    position: absolute; right: 19px; top: 243px; text-align: right;
    font-family: "Bebas Neue", sans-serif; font-size: 52px; line-height: 51px;
  }
  .headline__line--red { color: var(--red); }
  .headline__line--navy { color: var(--navy); }

  .photo {
    position: absolute; width: 114px; height: 114px; border: 3px solid var(--red);
    background: linear-gradient(180deg, var(--photo-light) 0%, #d3c6b6 55%, var(--photo-mid) 75%, var(--photo-dark) 100%);
  }
  .photo--navy { border-color: var(--navy); }

  .brand { position: absolute; display: flex; align-items: center; gap: 8px; color: var(--logo-grey); font-weight: 600; white-space: nowrap; }
  .brand__mark { background: var(--red); }
  .brand--small { left: 15px; top: 586px; font-size: 20px; }
  .brand--small .brand__mark { width: 16px; height: 16px; }
  .brand--large { left: 0; right: 0; top: 298px; justify-content: center; font-size: 31px; gap: 12px; }
  .brand--large .brand__mark { width: 24px; height: 24px; }

  .services {
    position: absolute; left: 0; right: 0; top: 640px; text-align: center;
    font-size: 13.6px; font-weight: 500; line-height: 23px;
  }
  .service-band {
    position: absolute; left: 0; right: 0; top: 724px; height: 44px;
    background: var(--navy); border-top: 2px solid var(--red); border-bottom: 2px solid var(--red);
    color: #fff; font-family: "Bebas Neue", sans-serif; font-size: 31px; line-height: 41px; text-align: center;
  }

  .contacts { position: absolute; left: 30px; top: 792px; list-style: none; font-size: 13.4px; font-weight: 500; line-height: 19px; }
  .contacts__item { position: relative; padding-left: 31px; margin-bottom: 15px; }
  .contacts__icon { position: absolute; left: 0; top: 0; width: 20px; height: 20px; }

  .slogan {
    position: absolute; left: 0; right: 0; top: 366px; text-align: center;
    color: var(--navy); font-size: 18px; font-weight: 600; line-height: 29px;
  }
  .divider { position: absolute; left: 13px; right: 13px; top: 443px; border-top: 2px dashed var(--red); }
</style>
</head>
<body>

<section class="hanger hanger--front">
  <svg class="hanger__cutout" width="332" height="200" aria-hidden="true">
    <path d="M0 97 H87 Q97 97 103 88 A71 71 0 1 1 103 126 Q97 117 87 117 H0 Z" fill="var(--stage)"/>
  </svg>

  <h1 class="headline">
    <span class="headline__line--red">Moulding</span><br>
    <span class="headline__line--red">Factory Outlet</span><br>
    <span class="headline__line--navy">Direct Sale</span>
  </h1>

  <div class="photo" style="left:26px;top:403px" role="img" aria-label="Kitchen and dining area with warm wood floor"></div>
  <div class="photo photo--navy" style="left:110px;top:448px" role="img" aria-label="Living room with trim work and wood floor"></div>
  <div class="photo" style="left:193px;top:503px" role="img" aria-label="Bright living room with feature wall and ceiling lights"></div>

  <div class="brand brand--small"><span class="brand__mark"></span>Ledge Crafts</div>

  <p class="services">Supply high quality Crown<br>mouldings, baseboards, casings<br>and wainscotings with competitive price</p>

  <div class="service-band">Installation &amp; Delivery</div>

  <ul class="contacts">
    <li class="contacts__item">
      <svg class="contacts__icon" viewBox="0 0 24 24" fill="none" stroke="var(--navy)" stroke-width="1.5"><path d="M5 3h4l2 5-2.5 1.5a11 11 0 0 0 6 6L16 13l5 2v4a2 2 0 0 1-2 2A17 17 0 0 1 3 5a2 2 0 0 1 2-2z"/></svg>
      416 555 0143 - 416 555 0187
    </li>
    <li class="contacts__item">
      <svg class="contacts__icon" viewBox="0 0 24 24" fill="none" stroke="var(--navy)" stroke-width="1.5"><rect x="2" y="5" width="20" height="14"/><path d="M2 5l10 8 10-8M2 19l7-7M22 19l-7-7"/></svg>
      info@ledgecrafts.example
    </li>
    <li class="contacts__item">
      <svg class="contacts__icon" viewBox="0 0 24 24" fill="none" stroke="var(--navy)" stroke-width="1.5"><path d="M12 22s7-7 7-13a7 7 0 0 0-14 0c0 6 7 13 7 13z"/><circle cx="12" cy="9" r="2.5"/></svg>
      47 North Willow Vale Rd, Richmond<br>Hill, ON L4B 3K9
    </li>
  </ul>
</section>

<section class="hanger hanger--back">
  <svg class="hanger__cutout" width="332" height="200" aria-hidden="true">
    <path d="M0 97 H87 Q97 97 103 88 A71 71 0 1 1 103 126 Q97 117 87 117 H0 Z" fill="var(--stage)"/>
  </svg>

  <div class="brand brand--large"><span class="brand__mark"></span>Ledge Crafts</div>

  <p class="slogan">Convert plain<br>room into designer’s interiors</p>
  <div class="divider"></div>

  <div class="photo" style="left:30px;top:479px" role="img" aria-label="Kitchen and dining area with wood floor"></div>
  <div class="photo photo--navy" style="left:188px;top:479px" role="img" aria-label="Living room with moulding detail"></div>
  <div class="photo photo--navy" style="left:30px;top:637px" role="img" aria-label="Living room with wainscoting wall"></div>
  <div class="photo" style="left:188px;top:637px" role="img" aria-label="Living room feature wall with ceiling lights"></div>

  <ul class="contacts">
    <li class="contacts__item">
      <svg class="contacts__icon" viewBox="0 0 24 24" fill="none" stroke="var(--navy)" stroke-width="1.5"><path d="M5 3h4l2 5-2.5 1.5a11 11 0 0 0 6 6L16 13l5 2v4a2 2 0 0 1-2 2A17 17 0 0 1 3 5a2 2 0 0 1 2-2z"/></svg>
      416 555 0143 - 416 555 0187
    </li>
    <li class="contacts__item">
      <svg class="contacts__icon" viewBox="0 0 24 24" fill="none" stroke="var(--navy)" stroke-width="1.5"><rect x="2" y="5" width="20" height="14"/><path d="M2 5l10 8 10-8M2 19l7-7M22 19l-7-7"/></svg>
      info@ledgecrafts.example
    </li>
    <li class="contacts__item">
      <svg class="contacts__icon" viewBox="0 0 24 24" fill="none" stroke="var(--navy)" stroke-width="1.5"><path d="M12 22s7-7 7-13a7 7 0 0 0-14 0c0 6 7 13 7 13z"/><circle cx="12" cy="9" r="2.5"/></svg>
      47 North Willow Vale Rd, Richmond<br>Hill, ON L4B 3K9
    </li>
  </ul>
</section>

</body>
</html>
```